Need wine label for brand that is named: Casmerel Vineyards & Winery

Casmerel is a yoga way of breathing. In Sanskrit Casmerel means "flying up." I would like a creative wine label that articulates Casmerel. The label should include a graphic and the name Casmerel on one line and Vineyards & Winery in smaller print underneath Casmerel.

```html
<!DOCTYPE html>
<html lang="en">
<head>
<meta charset="utf-8">
<title>Casmerel Vineyards &amp; Winery — Pinot Noir Label</title>
<link rel="stylesheet" href="https://fonts.googleapis.com/css2?family=Marcellus&family=Playfair+Display:wght@700&family=Cinzel:wght@400&display=swap">
<style>
  :root {
    --navy-deep: #0a1230;
    --navy-panel: #141d48;
    --navy-edge: #0c1535;
    --gold: #c9964a;
    --gold-light: #e2b774;
    --ivory: #ffffff;
    --rule: #e8e8ee;
  }
  html, body {
    margin: 0;
    padding: 0;
    width: 943px;
    height: 1200px;
    overflow: hidden;
    background: var(--navy-deep);
  }
  .label {
    position: relative;
    width: 943px;
    height: 1200px;
    background: var(--navy-deep);
    overflow: hidden;
  }
  .ornament {
    position: absolute;
    left: 160px;
    width: 624px;
    height: 162px;
  }
  .ornament--top {
    top: 32px;
    border-radius: 312px 312px 0 0 / 162px 162px 0 0;
    background: radial-gradient(ellipse at 50% 100%, var(--gold-light) 0%, var(--gold) 30%, rgba(201,150,74,0.35) 62%, rgba(10,18,48,0) 78%);
  }
  .ornament--bottom {
    top: 1006px;
    border-radius: 0 0 312px 312px / 0 0 162px 162px;
    background: radial-gradient(ellipse at 50% 0%, var(--gold-light) 0%, var(--gold) 30%, rgba(201,150,74,0.35) 62%, rgba(10,18,48,0) 78%);
  }
  .panel {
    position: absolute;
    left: 0;
    top: 194px;
    width: 943px;
    height: 810px;
    background: linear-gradient(90deg, var(--navy-edge) 0%, var(--navy-panel) 30%, var(--navy-panel) 70%, var(--navy-edge) 100%);
    border-top: 1.5px solid var(--rule);
    border-bottom: 1.5px solid var(--rule);
    box-sizing: border-box;
    text-align: center;
    color: var(--ivory);
  }
  .panel > * {
    position: absolute;
    left: 0;
    right: 0;
    margin: 0;
  }
  .brand-name {
    top: 52px;
    font-family: "Marcellus", serif;
    font-size: 84px;
    font-weight: 400;
    letter-spacing: 4px;
    color: var(--gold);
    line-height: 1;
  }
  .brand-sub {
    top: 170px;
    font-family: "Cinzel", serif;
    font-size: 25px;
    letter-spacing: 3px;
    line-height: 1;
  }
  .varietal {
    top: 240px;
    font-family: "Marcellus", serif;
    font-size: 66px;
    letter-spacing: 7px;
    line-height: 1;
  }
  .divider-mark {
    top: 359px;
    left: 433px;
    right: auto;
    width: 78px;
    height: 78px;
    border-radius: 50%;
    background: radial-gradient(circle, var(--gold-light) 0%, var(--gold) 45%, rgba(201,150,74,0) 72%);
  }
  .vintage {
    top: 512px;
    font-family: "Playfair Display", serif;
    font-weight: 700;
    font-size: 44px;
    letter-spacing: 6px;
    line-height: 1;
  }
  .collection {
    top: 568px;
    font-family: "Marcellus", serif;
    font-size: 50px;
    letter-spacing: 7px;
    line-height: 1;
  }
  .region {
    top: 634px;
    font-family: "Playfair Display", serif;
    font-weight: 700;
    font-size: 36px;
    letter-spacing: 5px;
    line-height: 1;
  }
  .abv {
    top: 748px;
    font-family: "Marcellus", serif;
    font-size: 21px;
    letter-spacing: 3px;
    color: var(--gold);
    line-height: 1;
  }
</style>
</head>
<body>
  <main class="label">
    <div class="ornament ornament--top" role="img" aria-label="Gold mandala ornament rising from the top band"></div>

    <section class="panel">
      <h1 class="brand-name">Casmerel</h1>
      <p class="brand-sub">Vineyards &amp; Winery</p>
      <h2 class="varietal">PINOT NOIR</h2>
      <div class="divider-mark" role="img" aria-label="Small gold four-petal mandala motif"></div>
      <p class="vintage">2014</p>
      <p class="collection">COLLECTION</p>
      <p class="region">Napa Valley</p>
      <p class="abv">11.8% alc/vol.</p>
    </section>

    <div class="ornament ornament--bottom" role="img" aria-label="Gold mandala ornament descending from the bottom band"></div>
  </main>
</body>
</html>
```